Pop punk gig poster design!

In need of an amazing poster design for a gig We are organising, the genre is pop punk, and will be an all ages gig. I need to it bold, random and capture the eye of any bypasses, and make people want to go to the gig just because the poster is awesome! The event will be called "A night of comets" and will consist of three bands and an acoustic set to open. All the bands are full of energy and create an unreal ambiance during there shows, I would like to capture that in the poster. Open to anything spectacular, the sky is the limit.

Requirements
Must have
• I need to have the name of the event "A Night Of Comets"
Band names(in this order):
-Turn the Dial
-Frozen Fenwick
-Wilma's Lantern
-Loralie Pettigrew

Date: Saturday 10th November 2012
Time: 5:15pm
Venue: The Kiln, 47 Tamsin street, West End, QLD 4101
Ticket price: $10+bf online
$15 at the door.
Free BBQ

```html
<!DOCTYPE html>
<html lang="en">
<head>
<meta charset="utf-8">
<title>A Night Of Comets – Gig Poster</title>
<link rel="stylesheet" href="https://fonts.googleapis.com/css2?family=Permanent+Marker&family=Federo&family=Antonio:wght@400&family=Sacramento&family=Lilita+One&display=swap">
<style>
  :root {
    --bg: #292929;
    --cyan: #35c3f0;
    --cyan-deep: #1590c4;
    --cyan-glow: #7fe0ff;
  }
  * { margin: 0; padding: 0; box-sizing: border-box; }
  html, body {
    width: 849px; height: 1200px; overflow: hidden; background: var(--bg);
  }
  .poster {
    position: relative; width: 849px; height: 1200px; overflow: hidden;
    background: var(--bg); color: var(--cyan);
  }
  .event-title { position: absolute; left: 16px; top: 6px; font-family: "Permanent Marker", cursive; line-height: 1; }
  .event-title .line-one { display: block; font-size: 84px; letter-spacing: 2px; text-transform: uppercase; }
  .event-title .line-two { display: block; margin-top: -8px; font-size: 84px; text-transform: uppercase; }
  .event-title .line-two small { font-size: 28px; margin-right: 2px; vertical-align: 22px; }
  .event-extra {
    position: absolute; left: 262px; top: 148px;
    font-family: "Permanent Marker", cursive; font-size: 34px; text-transform: uppercase; letter-spacing: 2px;
  }
  .lineup { position: absolute; left: 0; width: 849px; text-align: center; line-height: 1; white-space: nowrap; }
  .band-1 { top: 350px; font-family: "Federo", sans-serif; font-size: 66px; font-variant: small-caps; letter-spacing: 2px; }
  .band-2 { top: 420px; font-family: "Antonio", sans-serif; font-size: 92px; text-transform: uppercase; letter-spacing: 4px; }
  .band-3 { top: 516px; left: -40px; font-family: "Federo", sans-serif; font-size: 58px; text-transform: uppercase; letter-spacing: 1px; }
  .band-4 { top: 590px; font-family: "Sacramento", cursive; font-size: 98px; }
  .details { position: absolute; left: 0; width: 849px; text-align: center; font-family: "Lilita One", sans-serif; text-transform: uppercase; line-height: 1; white-space: nowrap; }
  .date-time { top: 748px; font-size: 43px; letter-spacing: 1px; }
  .venue { top: 815px; font-size: 30px; letter-spacing: 1px; }
  .tickets { top: 862px; font-size: 32px; letter-spacing: 1px; }
  .texture-field {
    position: absolute; left: 0; bottom: 0; width: 849px; height: 290px;
    background:
      radial-gradient(ellipse 40% 45% at 20% 85%, rgba(127,224,255,0.75), transparent 70%),
      radial-gradient(ellipse 35% 40% at 75% 80%, rgba(53,195,240,0.8), transparent 70%),
      radial-gradient(ellipse 30% 35% at 50% 100%, rgba(127,224,255,0.7), transparent 70%),
      linear-gradient(to bottom, rgba(41,41,41,0) 0%, rgba(21,144,196,0.35) 45%, var(--cyan-deep) 100%);
  }
</style>
</head>
<body>
<main class="poster">
  <h1 class="event-title">
    <span class="line-one">A Night</span>
    <span class="line-two"><small>of</small>Comets</span>
  </h1>
  <p class="event-extra">+ Free BBQ</p>

  <p class="lineup band-1">Turn the Dial</p>
  <p class="lineup band-2">Frozen Fenwick</p>
  <p class="lineup band-3">Wilma's Lantern</p>
  <p class="lineup band-4">Loralie Pettigrew</p>

  <p class="details date-time">Saturday 10th November 2012 | 5:15pm</p>
  <p class="details venue">The Kiln, 47 Tamsin Street, West End, QLD 4101</p>
  <p class="details tickets">Ticket price: $10 / $15 at the door</p>

  <div class="texture-field" role="img" aria-label="Cyan grunge brush texture rising from the bottom edge"></div>
</main>
</body>
</html>
```